Travel Blogger Business Card for roamquill.net

I need a two-sided business card for a travel blogging website. The card should be both professional and fun at the same time. This is for the website www.roamquill.net

I don't necessarily think that the current logo on the website needs to be used on the business card but it can be. I am very flexible with ideas

Target Market(s)

Travel agencies that will be met at a conference.

Industry/Entity Type

Travel

Contact Information for Business Card

Company Name: Roam Quill.net
Name: Bertrand Olesky
Voice: +1-(345)-402-7731
Address: Coral Reach Shore, Grand Cayman, Cayman Islands
Email: ceo@roamquill.net

Colors
0592cd
0355a3
3176b5
33a6d7
85cae6
85acd3

Requirements
Must have
• Website address and name should be bigger than address, phone number, and email.

```html
<!DOCTYPE html>
<html lang="en">
<head>
<meta charset="utf-8">
<title>Roam Quill.net — Business Card</title>
<link href="https://fonts.googleapis.com/css2?family=Montserrat:wght@400;500;800&family=Reenie+Beanie&display=swap" rel="stylesheet">
<style>
  :root {
    --card-blue: #0355a3;
    --band-blue: #85acd3;
    --icon-blue: #0355a3;
    --white: #ffffff;
    --ink: #111111;
    --page: #ffffff;
  }
  html, body {
    margin: 0;
    padding: 0;
    width: 1200px;
    height: 1000px;
    overflow: hidden;
    background: var(--page);
  }
  .canvas {
    position: relative;
    width: 1200px;
    height: 1000px;
    font-family: "Montserrat", sans-serif;
  }
  .card {
    position: absolute;
    top: 344px;
    width: 541px;
    height: 309px;
    background: var(--card-blue);
    overflow: hidden;
  }
  .card--front { left: 27px; }
  .card--back { left: 633px; width: 540px; }

  .brand {
    position: absolute;
    display: flex;
    align-items: center;
    color: var(--white);
    font-weight: 800;
    white-space: nowrap;
    letter-spacing: 0.5px;
  }
  .brand__dot {
    background: var(--white);
    border-radius: 50%;
    flex: none;
  }
  .card--front .brand { left: 14px; top: 50px; font-size: 24px; gap: 10px; }
  .card--front .brand__dot { width: 24px; height: 24px; }
  .card--back .brand { left: 0; right: 0; top: 122px; justify-content: center; font-size: 34px; gap: 14px; }
  .card--back .brand__dot { width: 34px; height: 34px; }

  .contact-list {
    position: absolute;
    left: 0;
    top: 120px;
    margin: 0;
    padding: 0;
    list-style: none;
  }
  .contact-item {
    position: relative;
    width: 299px;
    height: 38px;
    margin-bottom: 4px;
    background: var(--band-blue);
    display: flex;
    align-items: center;
    color: var(--ink);
    font-size: 13.5px;
    line-height: 1.15;
  }
  .contact-item__icon {
    position: absolute;
    left: 8px;
    top: 6px;
    width: 26px;
    height: 26px;
  }
  .contact-item__text { margin-left: 53px; }
  .contact-item--phone .contact-item__text { margin-left: 57px; }

  .holder-name {
    position: absolute;
    left: 310px;
    top: 158px;
    color: var(--white);
    font-family: "Reenie Beanie", cursive;
    font-size: 40px;
    white-space: nowrap;
  }
  .card--front .website {
    position: absolute;
    left: 0;
    width: 570px;
    top: 266px;
    text-align: center;
    color: var(--white);
    font-size: 20px;
    letter-spacing: 4.5px;
  }

  .back-tab {
    position: absolute;
    left: 0;
    bottom: 0;
    width: 540px;
    height: 69px;
  }
  .card--back .website {
    position: absolute;
    left: 0;
    right: 0;
    top: 262px;
    text-align: center;
    color: var(--ink);
    font-size: 21px;
    letter-spacing: 9.5px;
  }
</style>
</head>
<body>
<div class="canvas">

  <section class="card card--front" aria-label="Card front">
    <div class="brand"><span class="brand__dot"></span>ROAM QUILL.NET</div>

    <ul class="contact-list">
      <li class="contact-item contact-item--phone">
        <svg class="contact-item__icon" viewBox="0 0 26 26" aria-hidden="true">
          <circle cx="13" cy="13" r="13" fill="var(--icon-blue)"/>
          <path d="M8.5 7.5c.6-.6 1.4-.6 1.9 0l1.3 1.6c.4.5.4 1.2-.1 1.6l-.9.8c.7 1.6 1.9 2.8 3.5 3.5l.8-.9c.4-.5 1.1-.5 1.6-.1l1.6 1.3c.6.5.6 1.3 0 1.9l-.8.8c-.7.7-1.8.9-2.7.5-3.1-1.3-5.4-3.6-6.7-6.7-.4-.9-.2-2 .5-2.7z" fill="#fff"/>
        </svg>
        <span class="contact-item__text">+1-(345)-402-7731</span>
      </li>
      <li class="contact-item contact-item--email">
        <svg class="contact-item__icon" viewBox="0 0 26 26" aria-hidden="true">
          <circle cx="13" cy="13" r="13" fill="var(--icon-blue)"/>
          <rect x="6.5" y="8.5" width="13" height="9" fill="#fff"/>
          <path d="M6.5 8.5l6.5 5 6.5-5M6.5 17.5l4.6-4.2M19.5 17.5l-4.6-4.2" stroke="var(--icon-blue)" stroke-width="1.1" fill="none"/>
        </svg>
        <span class="contact-item__text">ceo@roamquill.net</span>
      </li>
      <li class="contact-item contact-item--address">
        <svg class="contact-item__icon" viewBox="0 0 26 26" aria-hidden="true">
          <circle cx="13" cy="13" r="13" fill="var(--icon-blue)"/>
          <path d="M13 20.5s-5-5.2-5-9a5 5 0 0 1 10 0c0 3.8-5 9-5 9z" fill="#fff"/>
          <circle cx="13" cy="11.3" r="1.9" fill="var(--icon-blue)"/>
        </svg>
        <span class="contact-item__text">Coral Reach Shore, Grand Cayman<br>Cayman Islands</span>
      </li>
    </ul>

    <div class="holder-name">Bertrand Olesky</div>
    <div class="website">www.roamquill.net</div>
  </section>

  <section class="card card--back" aria-label="Card back">
    <div class="brand"><span class="brand__dot"></span>ROAM QUILL.NET</div>
    <svg class="back-tab" viewBox="0 0 540 69" aria-hidden="true">
      <path d="M0 69 L32 18 Q43 0 64 0 L476 0 Q497 0 508 18 L540 69 Z" fill="var(--band-blue)"/>
    </svg>
    <div class="website">www.roamquill.net</div>
  </section>

</div>
</body>
</html>
```